Law Firm Logo and Stationary

I need a logo for my law firm.  The logo should only contain the firm name "Halvey & Halvey, P.C." but we are open to slight additions like underlining or a box.  We are looking for a modern style but not edgy because our target market is businesses and corporations.

I would like a logo that invokes the traditional values of a law firm (trust, integrity, knowledge) but I want an updated look.

To be clear, the logo should only contain the firm name, I am just looking for a font treatment.

The logo color is up to you.  The only initial opinion I have is that bright colors may not fit with the professional look of a law firm. 

I also want to incorporate the new logo into letterhead and business card designs.  The letterhead should include all of the information that is in my current letterhead, which is attached.  The letterhead should be black or grey on white.  The colored logo will go on the website and promotional materials.

For the business card, I would like to have the logo on the top left, the employee name (Colin T. Halvey) on the middle left and the firm information (address, tel, fax, website, email) on right side.  I am open to suggestions if you have better ideas.
Updates

Here are some comments on the initial 8 designs:

a) I am just interested in a font treatment of our firm name, "Halvey & Halvey, P.C."  I do not want any graphics like a gavel or shield. 

b) The full name of the firm must be in the logo.  So I cannot use designs that only have "H & H"

c) EXAMPLES: Here are two websites with examples of law firm logos that just have the firm name.  These are just samples to give you a general idea of what I am looking for.  Check out:  www.qz-legal.example and www.marrowfieldtate.example 

In short, I am looking for a simple, clean design that will look modern enough for our website but is also conservative enough to be on letterhead that gets sent to judges and other lawyers.

Also, the sample letterhead is now loaded in the brief so you can see the information I need included in the new letterhead.

Thanks.

Target Market(s)

businesses and corporations.

Industry/Entity Type

Law Firm

Logo Text

Halvey & Halvey, P.C.

Requirements
Must have
• Firm name, "Halvey & Halvey, P.C."

```html
<!DOCTYPE html>
<html lang="en">
<head>
<meta charset="utf-8">
<title>Halvey &amp; Halvey, P.C. – Identity Sheet</title>
<link href="https://fonts.googleapis.com/css2?family=Stint+Ultra+Condensed&display=swap" rel="stylesheet">
<style>
  :root {
    --brown: #5b4a40;
    --tan: #b0a58b;
    --paper: #ffffff;
    --rule: #4a3f38;
  }
  html, body { margin: 0; padding: 0; overflow: hidden; }
  body { width: 848px; height: 1200px; background: var(--paper); position: relative;
         font-family: "Stint Ultra Condensed", "Arial Narrow", serif; color: var(--brown); }
  .wordmark { position: absolute; display: block; overflow: visible; }
  .wordmark text { font-family: "Stint Ultra Condensed", "Arial Narrow", serif; fill: var(--brown); }
  .wordmark--hero { left: 72px; top: 96px; width: 470px; height: 100px; }

  .letterhead { position: absolute; left: 138px; top: 244px; width: 624px; height: 882px;
                border: 1px solid var(--rule); }
  .letterhead .wordmark--head { left: 12px; top: 48px; width: 196px; height: 40px; }
  .letterhead__divider { position: absolute; left: 214px; top: 28px; width: 1px; height: 89px; background: var(--brown); }
  .letterhead__masthead { position: absolute; left: 223px; top: 44px; line-height: 1; color: var(--brown); }
  .masthead__title { font-size: 16px; letter-spacing: 0.08em; margin: 0 0 2px; font-weight: 400; }
  .masthead__line { font-size: 8px; letter-spacing: 0.06em; margin: 0; line-height: 9px; }
  .letterhead__footer { position: absolute; left: 21px; top: 770px; font-size: 14px; font-style: normal;
                        line-height: 15.2px; letter-spacing: 0.06em; }

  .business-card { position: absolute; left: 417px; top: 498px; width: 379px; height: 186px;
                   border: 1px solid var(--rule); background: var(--paper); }
  .business-card__details { position: absolute; left: 0; top: 0; width: 198px; height: 187px;
                            background: var(--brown); color: var(--tan); }
  .business-card__name { position: absolute; left: 26px; top: 48px; margin: 0; font-size: 16px;
                         font-weight: 400; color: var(--paper); letter-spacing: 0.07em; }
  .business-card__contact { position: absolute; left: 26px; top: 68px; font-size: 11.5px; font-style: normal;
                            line-height: 13.5px; letter-spacing: 0.05em; }
  .business-card .wordmark--card { left: 210px; top: 78px; width: 158px; height: 34px; }
</style>
</head>
<body>

<svg class="wordmark wordmark--hero" viewBox="0 0 470 100" aria-label="Halvey &amp; Halvey, P.C.">
  <text x="0" y="92" font-size="118" textLength="470" lengthAdjust="spacingAndGlyphs">Halvey &amp; Halvey, P.C.</text>
</svg>

<section class="letterhead">
  <svg class="wordmark wordmark--head" viewBox="0 0 196 40" aria-label="Halvey &amp; Halvey, P.C.">
    <text x="0" y="36" font-size="46" textLength="196" lengthAdjust="spacingAndGlyphs">Halvey &amp; Halvey, P.C.</text>
  </svg>
  <div class="letterhead__divider"></div>
  <div class="letterhead__masthead">
    <h2 class="masthead__title">LAW OFFICES</h2>
    <p class="masthead__line">MARTIN J. HALVEY</p>
    <p class="masthead__line">COLIN T. HALVEY</p>
    <p class="masthead__line">WALTER HALVEY (1921-1998)</p>
    <p class="masthead__line">Admitted to practice District of Columbia . Maryland . New York</p>
  </div>
  <address class="letterhead__footer">
    2150 Linden Avenue<br>
    Fairhaven, MD 20999<br>
    T: 555.014.2671<br>
    F: 555.014.9038<br>
    E: martin.halvey@halveypc.example<br>
    www.halveypc.example
  </address>
</section>

<section class="business-card">
  <div class="business-card__details">
    <h3 class="business-card__name">MARTIN J. HALVEY</h3>
    <address class="business-card__contact">
      2150 Linden Avenue<br>
      Fairhaven, MD 20999<br>
      T: 555.014.2671<br>
      F: 555.014.9038<br>
      E: martin.halvey@halveypc.example<br>
      www.halveypc.example
    </address>
  </div>
  <svg class="wordmark wordmark--card" viewBox="0 0 158 34" aria-label="Halvey &amp; Halvey, P.C.">
    <text x="0" y="30" font-size="38" textLength="158" lengthAdjust="spacingAndGlyphs">Halvey &amp; Halvey, P.C.</text>
  </svg>
</section>

</body>
</html>
```